"The Wandering Mentor", a Higher Ed blogger, would like a wordpress design

I would like a wordpress design for blogs written by "The Wandering Mentor." that can be easily expanded by me once the initial design is complete.

Here is context which I would like included on the Home/Welcome page: "I started The Wandering Mentor in 2021 to write about the practice of academic advising through the lens of horsemanship. After one year of developing skills as a brand new equestrian, I couldn’t help but notice the similarities between my vocation as an academic advisor and my avocation as a budding equestrian. I hope my musings about my journey in two very different fields will cultivate curiosity, widen your aperture and ignite academic advisors to take their practice to the next level. "

The wordpress will primarily have blogs by myself or guest bloggers writing about academic advising for advisors, but I may widen my audience to include students and families. I'd like to have readers submit questions that I can answer. Depending on interest, I may want to have a section on Horsemanship but that is not truly the focus of this site.

I'd like the feel of the site to be positive, fresh, modern (but not too wild), with the emphasis on Higher Ed/Academic Advising as opposed to equestrian pursuits. I don't want it to feel clunky and blocky like some sites that have to do with education. I'm hoping that readers will have some "aha" moments after reading some of the posts.

I have included my logo files

```html
<!DOCTYPE html>
<html lang="en">
<head>
<meta charset="utf-8">
<title>The Wandering Mentor</title>
<link href="https://fonts.googleapis.com/css2?family=Alegreya+SC:wght@400;500;700&family=Alegreya:wght@400;500&family=Poppins:wght@300;400;500&display=swap" rel="stylesheet">
<style>
:root{
  --gold:#d7a95c;
  --tan:#dcaf68;
  --tan-light:#e9c98f;
  --cream:#f6ead4;
  --ink:#1e1e1e;
  --dark:#222222;
  --text:#555555;
  --muted:#666666;
  --white:#ffffff;
}
*{box-sizing:border-box;margin:0;padding:0}
html,body{width:1200px;height:4023px;overflow:hidden}
body{position:relative;background:var(--white);font-family:'Poppins',sans-serif;color:var(--text)}
.abs{position:absolute}
.serif{font-family:'Alegreya SC',serif}

/* top bar */
.topbar{left:0;top:0;width:1200px;height:39px;background:var(--ink);color:#e8e8e8;font-size:13px}
.topbar .social{left:110px;top:8px;display:flex;gap:6px}
.topbar .social span{width:23px;height:23px;border:1.5px solid #ddd;border-radius:50%;display:block}
.topbar .contact{right:112px;top:10px;display:flex;gap:20px;font-size:13px}

/* hero */
.hero{left:0;top:39px;width:1200px;height:711px}
.hero-photo{left:0;top:0;width:1200px;height:680px;background:linear-gradient(100deg,#5d4a3c 0%,#3a2e28 35%,#2a2320 55%,#6b3f22 75%,#8a5530 100%)}
.header-shade{left:0;top:0;width:1200px;height:170px;background:rgba(20,18,16,.55)}
.brand{left:0;top:42px;width:1200px;text-align:center;font-family:'Alegreya SC',serif;font-weight:500;font-size:24px;color:var(--gold);letter-spacing:1px}
.brand .ring{display:inline-block;width:14px;height:14px;border:2px solid var(--gold);border-radius:50%;margin-right:10px;vertical-align:middle}
.nav{left:0;top:136px;width:1200px;display:flex;justify-content:center;gap:17px;font-family:'Alegreya SC',serif;font-weight:700;font-size:16px;color:#fff}
.nav .active{color:var(--gold)}
.hero-title{left:0;top:310px;width:1200px;text-align:center;font-family:'Alegreya SC',serif;font-weight:500;font-size:48px;color:#fff;letter-spacing:1px}
.hero-sub{left:0;top:378px;width:1200px;text-align:center;font-size:21px;color:#fff}
.dots{left:0;top:574px;width:1200px;display:flex;justify-content:center;gap:11px}
.dots span{width:15px;height:15px;border:2px solid var(--gold);border-radius:50%}
.dots .on{background:var(--gold)}
.hero-wave{left:0;top:600px}

/* section heading */
.heading{left:0;width:1200px;display:flex;justify-content:center;align-items:center;gap:10px;font-family:'Alegreya',serif;font-size:29px;text-transform:uppercase}
.heading .rule{width:48px;height:5px;border-top:1.5px solid currentColor;border-bottom:1.5px solid currentColor}

/* welcome */
.welcome-h{top:794px;color:var(--gold)}
.welcome-h .rule{color:#666}
.welcome-sub{left:0;top:846px;width:1200px;text-align:center;font-family:'Alegreya',serif;font-size:19px;color:var(--dark)}
.welcome-copy{left:140px;top:902px;width:920px;text-align:center;font-size:16.5px;font-weight:300;line-height:30px;color:var(--text)}

/* services */
.services{left:0;top:1152px;width:1200px;height:1078px;background:var(--tan)}
.services-h{top:90px;color:var(--dark)}
.svc-photo{width:350px;height:350px;border-radius:50%}
.svc-ring{width:374px;height:374px}
.svc-badge{width:90px;height:90px;border-radius:50%;background:#fff;display:flex;align-items:center;justify-content:center}
.svc-title{font-size:28px;color:#fff;font-weight:400}
.svc-copy{width:500px;font-size:16px;line-height:30px;color:#fff;font-weight:300}
.btn{height:50px;padding:0 22px;background:var(--ink);color:#fff;border-radius:25px;display:flex;align-items:center;gap:10px;font-size:15px;font-weight:500}

/* blogs */
.blogs-h{top:2310px;color:var(--gold)}
.blogs-h .rule{color:#777}
.card{top:2427px;width:228px;height:395px;border-radius:114px;background:#fff;box-shadow:0 6px 18px rgba(0,0,0,.12)}
.card .thumb{left:14px;top:10px;width:200px;height:200px;border-radius:50%}
.card .date{left:83px;top:170px;width:62px;height:62px;border-radius:50%;background:var(--gold);color:#fff;font-size:9px;line-height:12px;text-align:center;padding-top:16px}
.card .date i{display:block;width:12px;height:10px;border:1.5px solid #fff;margin:0 auto 3px;border-radius:2px}
.card h3{left:0;top:248px;width:228px;text-align:center;font-weight:400;font-size:16.5px;line-height:21px;color:var(--dark)}
.card p{left:0;top:300px;width:228px;text-align:center;font-size:14px;line-height:20px;color:var(--muted)}
.card .arrow{left:99px;top:358px}

/* call back */
.callback{left:0;top:2938px;width:1200px;height:560px}
.cb-photo{left:0;top:0;width:600px;height:560px;background:linear-gradient(180deg,#4d6a3d 0%,#6e8a4c 35%,#a08549 62%,#c9a05c 100%)}
.cb-tan{left:600px;top:0;width:600px;height:560px;background:#e4bd7f}
.play{left:274px;top:256px;width:56px;height:56px;border-radius:50%;background:#fff}
.form{left:459px;top:67px;width:479px;height:426px;background:#fff;border-radius:4px}
.form-h{left:0;top:48px;width:479px;color:var(--dark);font-size:23px}
.form-h .rule{width:50px}
.field{height:40px;border:1px solid #e2c48e;border-radius:5px;font-size:11px;color:#999;padding:12px 12px}

/* footer */
.footer{left:0;top:3440px;width:1200px;height:583px;background:#1d1d1d}
.fnav{left:0;top:200px;width:1200px;display:flex;justify-content:center;align-items:center;gap:22px;font-family:'Alegreya SC',serif;font-weight:700;font-size:15px;color:var(--gold)}
.fnav b{width:4px;height:4px;border-radius:50%;background:var(--gold)}
.frule{left:112px;top:265px;width:976px;height:1px;background:#444}
.fcol{top:300px;width:300px;text-align:center;color:#ddd;font-size:13px;line-height:21px}
.fcol h4{font-family:'Alegreya SC',serif;font-weight:500;font-size:16px;color:var(--gold);margin-bottom:8px}
.fsep{top:288px;width:1px;height:130px;background:#555}
.fsocial{display:flex;justify-content:center;gap:12px;margin-top:14px}
.fsocial span{width:36px;height:36px;border:1.5px solid #ddd;border-radius:50%}
.copyright{left:0;top:3952px;width:1200px;text-align:center;font-size:13px;color:#ddd}
</style>
</head>
<body>

<!-- top bar -->
<div class="abs topbar">
  <div class="abs social" aria-label="Social links"><span></span><span></span><span></span></div>
  <div class="abs contact"><span>Phone: 123-456-7890</span><span>Email: hello@wanderingmentor.example</span></div>
</div>

<!-- hero -->
<section class="abs hero">
  <div class="abs hero-photo" role="img" aria-label="Photo of a rider in a helmet greeting a brown horse in a sunlit arena"></div>
  <div class="abs header-shade"></div>
  <div class="abs brand"><span class="ring"></span>The Wandering Mentor</div>
  <nav class="abs nav"><span class="active">Home</span><span>About</span><span>Services</span><span>Blogs</span><span>FAQs</span><span>Bookings</span></nav>
  <h1 class="abs hero-title">The Wandering Mentor</h1>
  <p class="abs hero-sub">sed do eiusmod tempor incididunt ut labore</p>
  <div class="abs dots"><span></span><span class="on"></span><span></span></div>
  <svg class="abs hero-wave" width="1200" height="150" viewBox="0 0 1200 150">
    <path d="M0 60 C250 20 420 40 640 75 C860 110 1050 80 1200 20 L1200 150 L0 150Z" fill="#e6c58b"/>
    <path d="M0 80 C260 35 440 70 660 95 C880 120 1060 105 1200 55 L1200 150 L0 150Z" fill="#f3e3c6"/>
    <path d="M0 100 C270 55 460 95 680 112 C900 128 1070 125 1200 90 L1200 150 L0 150Z" fill="#fff"/>
  </svg>
</section>

<!-- welcome -->
<div class="abs heading welcome-h"><span class="rule"></span>Welcome<span class="rule"></span></div>
<p class="abs welcome-sub">THE WANDERING MENTOR</p>
<p class="abs welcome-copy">I started The Wandering Mentor in 2021 to write about the practice of academic advising through the lens of horsemanship. After one year of developing skills as a brand new equestrian, I couldn't help but notice the similarities between my vocation as an academic advisor and my avocation as a budding equestrian. I hope my musings about my journey in two very different fields will cultivate curiosity, widen your aperture and ignite academic advisors to take their practice to the next level.</p>

<!-- services -->
<section class="abs services">
  <div class="abs heading services-h"><span class="rule"></span>Services<span class="rule"></span></div>

  <svg class="abs svc-ring" style="left:150px;top:184px" viewBox="0 0 374 374"><path d="M40 300 A180 180 0 1 0 140 25" fill="none" stroke="#111" stroke-width="5"/></svg>
  <div class="abs svc-photo" style="left:160px;top:195px;background:radial-gradient(circle at 45% 55%,#9a5a2e,#5a3420 60%,#d9c7a8 100%)" role="img" aria-label="Photo of a rider in boots mounted on a bay horse"></div>
  <div class="abs svc-badge" style="left:163px;top:190px">
    <svg width="48" height="40" viewBox="0 0 48 40" fill="none" stroke="#d7a95c" stroke-width="2.5" stroke-linejoin="round"><path d="M2 14 L24 4 L46 14 L24 24Z"/><path d="M11 18 V28 C17 34 31 34 37 28 V18"/><path d="M44 15 V28"/></svg>
  </div>
  <h2 class="abs svc-title" style="left:591px;top:252px">Vocation as an Academic Advisor</h2>
  <p class="abs svc-copy" style="left:591px;top:298px">Sed ut perspiciatis unde omnis iste natus error sit voluptatem accusantium doloremque laudantium, totam rem aperiam, eaque ipsa quae ab illo inventore veritatis et quasi architecto beatae vitae dicta sunt explicabo.</p>
  <div class="abs btn" style="left:591px;top:437px">LEARN MORE
    <svg width="28" height="12" viewBox="0 0 28 12" fill="none" stroke="#fff" stroke-width="2"><path d="M0 6H26M21 1L26 6L21 11"/></svg></div>

  <h2 class="abs svc-title" style="left:120px;top:672px">Vocation as a Budding Equestrian</h2>
  <p class="abs svc-copy" style="left:120px;top:717px">Sed ut perspiciatis unde omnis iste natus error sit voluptatem accusantium doloremque laudantium, totam rem aperiam, eaque ipsa quae ab illo inventore veritatis et quasi architecto beatae vitae dicta sunt explicabo.</p>
  <div class="abs btn" style="left:120px;top:856px">LEARN MORE
    <svg width="28" height="12" viewBox="0 0 28 12" fill="none" stroke="#fff" stroke-width="2"><path d="M0 6H26M21 1L26 6L21 11"/></svg></div>

  <svg class="abs svc-ring" style="left:674px;top:604px" viewBox="0 0 374 374"><path d="M10 230 A180 180 0 1 0 140 25" fill="none" stroke="#111" stroke-width="5"/></svg>
  <div class="abs svc-photo" style="left:684px;top:614px;background:radial-gradient(circle at 50% 60%,#6a4330,#4a3226 55%,#c9b59a 100%)" role="img" aria-label="Photo of an older rider and a young girl with a horse in a stable"></div>
  <div class="abs svc-badge" style="left:687px;top:608px;width:86px;height:86px"></div>
</section>

<!-- latest blogs -->
<div class="abs heading blogs-h"><span class="rule"></span>Latest Blogs<span class="rule"></span></div>

<article class="abs card" style="left:166px">
  <div class="abs thumb" style="background:linear-gradient(160deg,#a77b52,#e2d4c2 60%,#8a6a4d)" role="img" aria-label="Photo of a child hugging a pony"></div>
  <div class="abs date"><i></i>13 sep,<br>2021</div>
  <h3 class="abs">Temporibus autem quibusdam et aut officiis</h3>
  <p class="abs">debitis aut rerum nece ssitatib saepe eveniet</p>
  <svg class="abs arrow" width="30" height="14" viewBox="0 0 30 14" fill="none" stroke="#d7a95c" stroke-width="2"><path d="M1 7H28M22 1L28 7L22 13"/></svg>
</article>
<article class="abs card" style="left:486px">
  <div class="abs thumb" style="background:linear-gradient(180deg,#4a4a44,#8b8576 45%,#cfc5b0 100%)" role="img" aria-label="Photo of show jumping poles in a sand arena"></div>
  <div class="abs date"><i></i>13 sep,<br>2021</div>
  <h3 class="abs">Temporibus autem quibusdam et aut officiis</h3>
  <p class="abs">debitis aut rerum nece ssitatib saepe eveniet</p>
  <svg class="abs arrow" width="30" height="14" viewBox="0 0 30 14" fill="none" stroke="#d7a95c" stroke-width="2"><path d="M1 7H28M22 1L28 7L22 13"/></svg>
</article>
<article class="abs card" style="left:806px">
  <div class="abs thumb" style="background:linear-gradient(120deg,#dfe3e6,#b9c0c4 45%,#4b3327 100%)" role="img" aria-label="Photo of a veterinarian examining a horse"></div>
  <div class="abs date"><i></i>13 sep,<br>2021</div>
  <h3 class="abs">Temporibus autem quibusdam et aut officiis</h3>
  <p class="abs">debitis aut rerum nece ssitatib saepe eveniet</p>
  <svg class="abs arrow" width="30" height="14" viewBox="0 0 30 14" fill="none" stroke="#d7a95c" stroke-width="2"><path d="M1 7H28M22 1L28 7L22 13"/></svg>
</article>

<!-- request call back -->
<section class="abs callback">
  <div class="abs cb-photo" role="img" aria-label="Video still of a rider galloping a chestnut horse across a field"></div>
  <div class="abs play"><svg width="56" height="56" viewBox="0 0 56 56"><path d="M23 18 L38 28 L23 38Z" fill="#cfcfcf"/></svg></div>
  <div class="abs cb-tan"></div>
  <form class="abs form">
    <div class="abs heading form-h"><span class="rule"></span>Request Call Back<span class="rule"></span></div>
    <div class="abs field" style="left:64px;top:114px;width:171px">Name</div>
    <div class="abs field" style="left:247px;top:114px;width:171px">Email</div>
    <div class="abs field" style="left:64px;top:168px;width:171px">Phone</div>
    <div class="abs field" style="left:247px;top:168px;width:171px">Address</div>
    <div class="abs field" style="left:64px;top:223px;width:354px;height:70px">Message</div>
    <div class="abs btn" style="left:64px;top:315px;height:50px;font-size:14px">SUBMIT NOW
      <svg width="28" height="12" viewBox="0 0 28 12" fill="none" stroke="#fff" stroke-width="2"><path d="M0 6H26M21 1L26 6L21 11"/></svg></div>
  </form>
</section>

<!-- footer -->
<footer class="abs footer">
  <svg class="abs" style="left:0;top:-60px" width="1200" height="130" viewBox="0 0 1200 130">
    <path d="M0 130 L0 80 C200 20 420 10 640 40 C860 70 1040 60 1200 0 L1200 130Z" fill="#3a3a3a"/>
    <path d="M0 130 L0 100 C220 40 430 40 650 65 C870 90 1050 85 1200 30 L1200 130Z" fill="#1d1d1d"/>
  </svg>
  <nav class="abs fnav"><span>Home</span><b></b><span>About</span><b></b><span>Services</span><b></b><span>Blogs</span><b></b><span>FAQs</span><b></b><span>Bookings</span></nav>
  <div class="abs frule"></div>
  <div class="abs fcol" style="left:114px">
    <h4>Get Social</h4>
    <p>follo us on social media</p>
    <div class="fsocial" aria-label="Social links"><span></span><span></span><span></span></div>
  </div>
  <div class="abs fsep" style="left:426px"></div>
  <div class="abs fcol" style="left:450px">
    <h4>We Are Here</h4>
    <p>The Wandering Mentor, 234 miles,<br>demo address<br>Phone : 123-456-7890<br>Email : hello@wanderingmentor.example</p>
  </div>
  <div class="abs fsep" style="left:769px"></div>
  <div class="abs fcol" style="left:778px">
    <h4>We Are Here</h4>
    <p>Privacy Policy<br>Terms &amp; Conditions</p>
  </div>
</footer>
<p class="abs copyright">© 2021 The Wandering Mentor. All Rights Reserved.</p>

</body>
</html>
```